IT Freelancer (Consulting, trainer and project manager) needed letterhead

As a freelancer for IT Trainingswhip, consulting and project management I need a letterhead design. What is desired is a design that fits the existing logo (see Annex). It is functional, reliable, and equal time wirkenn Agil and modern. The whole is in color, as well as printed out to make a good impression on a black and white printer. The whole is to the existing Cooperate design (business card, homepage, logo) fit. Therefore, the choice of colors.
Updates

Target Market(s)

Customers such as medium-sized enterprises, training institutions

Industry/Entity Type

Consulting

Colors
0455a3
3277b5
85abd2
cfdfed
34a6d7
32a6d6
249fd4
0792cd
85cae6

Requirements
Must have
• Must include logo (see Annex) address (Brennerweg 14, 94871 Lindenfeld, Germany). Must seriously and act simultaneously Agil. Design should (even) be adaptable (signature, address, etc.) design must look good on a black / white laser

```html
<!DOCTYPE html>
<html lang="en">
<head>
<meta charset="utf-8">
<title>Konrad Selmer – Letterhead</title>
<link href="https://fonts.googleapis.com/css2?family=Lato:wght@400;700&display=swap" rel="stylesheet">
<style>
  :root {
    --navy: #0455a3;
    --sky: #34a6d7;
    --ink: #555a60;
    --paper: #ffffff;
  }
  * { margin: 0; padding: 0; box-sizing: border-box; }
  html, body { width: 800px; height: 1200px; overflow: hidden; background: var(--paper); }
  .letterhead {
    position: relative;
    width: 800px;
    height: 1200px;
    background: var(--paper);
    font-family: "Lato", Arial, sans-serif;
  }
  .header-block {
    position: absolute;
    left: 0; top: 0;
    width: 78px; height: 133px;
    background: var(--navy);
  }
  .brand-badge {
    position: absolute;
    left: 42px; top: 15px;
    width: 104px; height: 104px;
    border-radius: 50%;
    background: var(--paper);
  }
  .brand-badge::after {
    content: "";
    position: absolute;
    left: 7px; top: 7px;
    width: 90px; height: 90px;
    border-radius: 50%;
    background: var(--navy);
  }
  .brand-name {
    position: absolute;
    left: 152px; top: 44px;
    color: var(--navy);
    font-weight: 700;
    font-size: 22px;
    line-height: 22px;
    letter-spacing: 0.5px;
  }
  .header-rule {
    position: absolute;
    left: 89px; top: 122px;
    width: 711px; height: 9px;
    background: var(--sky);
  }
  .footer-rules {
    position: absolute;
    left: 0; top: 1096px;
    width: 800px; height: 8px;
  }
  .footer-contact {
    position: absolute;
    left: 0; top: 1122px;
    width: 800px;
    text-align: center;
    color: var(--ink);
    font-size: 13px;
    line-height: 26px;
  }
  .footer-contact .label { color: var(--navy); font-weight: 700; }
  .footer-contact .sep { margin: 0 4px; }
</style>
</head>
<body>
  <div class="letterhead">
    <div class="header-block"></div>
    <div class="brand-badge"></div>
    <div class="brand-name">KONRAD<br>SELMER</div>
    <div class="header-rule"></div>

    <svg class="footer-rules" width="800" height="8" viewBox="0 0 800 8">
      <polygon points="0,0 400,0 403,8 0,8" fill="#34a6d7"/>
      <polygon points="407,2 800,2 800,8 409,8" fill="#0455a3"/>
    </svg>

    <div class="footer-contact">
      <p>
        <span class="label">Phone:</span> 1378 40219<span class="sep">|</span>
        <span class="label">Email:</span> kontakt@selmer-it.de<span class="sep">|</span>
        <span class="label">Web:</span> www.selmer-it.de
      </p>
      <p>Brennerweg 14, 94871 Lindenfeld, Germany</p>
    </div>
  </div>
</body>
</html>
```